Vinto PR Website

Vinto PR are a PR company with a requirement for a new website. In consultation with the client, we have defined a wireframe for a homepage to show content and functionality. A PDF of the wire frame is attached.
Current site http://www.vinto-pr.co.uk/
Updates
If you are using Stock Photography - please use PixVault
Dear All
Unfortunately, my client didn't like any of the designs submitted.
I've uploaded 3 examples of the type of photography that will appear in the carousel as supplied by the client.
Target Market(s)
Business to Business/Professionals - high value clients
Number of Pages Required
1 page
Requirements
Must have
- Colour scheme is attached as a .ase file from Kuler and can be viewed on Kuler if you search for 'VINTO PR Palette'
Corporate Typeface is Futura Book - use of Cufon is OK
Current Logo to be reatainedCall 2 Action Buttons will be controlled via the CMS so a generic background may be useful for these.
Nice to have
- RSS feeds

```html
<!DOCTYPE html>
<html lang="en">
<head>
<meta charset="utf-8">
<title>Vinto PR</title>
<link rel="stylesheet" href="https://fonts.googleapis.com/css2?family=Arimo:wght@400;700&family=Jost:wght@400&display=swap">
<style>
:root{
  --page:#ebebeb;
  --white:#ffffff;
  --teal:#6fc1b3;
  --teal-dark:#5aab9d;
  --teal-pale:#eef8f6;
  --teal-active:#8ed8cc;
  --footer:#7ab5a3;
  --footer-bar:#49654f;
  --heading:#3f6e56;
  --news-heading:#6aab97;
  --phone:#1d84c6;
  --text:#222222;
  --muted:#999999;
  --panel:#f1f1f1;
}
*{margin:0;padding:0;box-sizing:border-box}
html,body{width:960px;height:1200px;overflow:hidden}
body{background:var(--page);font-family:Arimo,Arial,sans-serif;color:var(--text);position:relative}
a{color:inherit;text-decoration:none}
.abs{position:absolute}

.social-bar{left:525px;top:0;width:341px;height:29px;background:#e2e2e2;border-radius:0 0 6px 6px;display:flex;align-items:center;padding-left:8px;font-size:9px}
.social-bar .item{display:flex;align-items:center;gap:6px;padding:0 10px;border-right:1px solid #bbb;color:#666;text-decoration:underline}
.social-bar .item:last-child{border-right:none}
.social-bar .dot{width:14px;height:14px;border-radius:3px;display:inline-block}

.sheet{left:98px;top:40px;width:768px;height:870px;background:var(--white)}
.brand-name{left:134px;top:74px;font-family:Jost,sans-serif;font-weight:400;font-size:20px;color:#333}
.call{right:112px;top:70px;font-family:Jost,sans-serif;font-size:15px;color:#aaa}
.call strong{font-weight:400;font-size:22px;color:var(--phone);letter-spacing:.5px}

.nav{left:96px;top:132px;width:770px;height:30px;background:linear-gradient(#7fcbbe,var(--teal-dark));display:flex;align-items:center;padding-left:20px;font-size:11px;color:#fff;box-shadow:0 3px 4px rgba(0,0,0,.12)}
.nav a{padding:0 16px;border-right:1px solid rgba(255,255,255,.25);line-height:30px}
.nav a:last-child{border:none}
.nav a.current{color:#333}

.banner{left:120px;top:186px;width:721px;height:200px}
.service-menu{position:absolute;left:0;top:0;width:175px;height:200px;background:var(--teal-pale)}
.service-menu a{position:absolute;left:20px;font-size:11.5px;color:#111}
.service-menu a.active{left:0;width:175px;height:28px;background:var(--teal-active);color:#fff;padding-left:20px;line-height:28px}
.carousel{position:absolute;left:175px;top:0;width:546px;height:200px;background:linear-gradient(135deg,#c7d9d6,#e7efee 55%,#c2d6d3)}
.carousel h2{position:absolute;top:68px;width:100%;text-align:center;font-family:Jost,sans-serif;font-weight:400;font-size:17px;color:#111}
.carousel p{position:absolute;top:111px;width:100%;text-align:center;font-family:Jost,sans-serif;font-size:9.5px;color:#111}

.intro{left:114px;top:410px;width:480px;height:291px;background:#fdfdfd;padding:16px 18px}
.intro h1{font-weight:400;font-size:19px;color:var(--heading);letter-spacing:1px;margin-bottom:17px}
.intro p{font-size:9.5px;line-height:19.2px;letter-spacing:.5px;margin-bottom:19px}

.news{top:722px;width:231px;height:145px;background:var(--panel);padding:10px 14px}
.news h3{font-weight:400;font-size:16px;color:var(--news-heading);letter-spacing:.5px;border-bottom:1px solid #fff;padding-bottom:5px;margin-bottom:10px;display:flex;justify-content:space-between;align-items:center}
.news p{font-size:9px;line-height:14.4px;letter-spacing:.6px;color:#444}
.news .more{display:inline-block;font-size:8px;color:var(--news-heading);border-bottom:1px solid var(--news-heading);margin-top:6px}
.blog-img{float:right;width:88px;height:66px;margin:0 0 4px 8px;background:linear-gradient(135deg,#6aa5d8,#9ed1c0 60%,#3e7fb8)}

.c2a{left:626px;width:199px;height:98px;color:#fff;font-size:11px;padding:6px}
.c2a-1{top:430px;background:linear-gradient(135deg,#d9dadb,#f2f2f2 50%,#c94b43)}
.c2a-2{top:538px;background:linear-gradient(90deg,#8f8f8f,#d3d3d3 60%,#9a9a9a)}
.c2a-3{top:645px;background:linear-gradient(135deg,#e2757a,#f4c6c7 50%,#d65a60)}
.c2a-4{top:753px;background:linear-gradient(90deg,#f4f4f4,#e6e6e6 55%,#c9a58c)}

.footer{left:98px;top:910px;width:768px;height:144px;background:var(--footer)}
.footer-links{top:934px;font-size:10px;color:#fff;line-height:19.2px;letter-spacing:.3px}
.enews{left:625px;top:930px;width:209px;height:108px;background:#93c3b5;padding:8px 9px}
.enews h4{font-weight:400;font-size:13px;color:#fff;letter-spacing:.5px;margin-bottom:12px}
.enews .field{width:190px;height:19px;background:#f4f4f4;border:1px solid #ccc;font-size:8.5px;color:#666;padding:4px 7px}
.enews .btn{margin-top:16px;width:78px;height:24px;background:#9fe0d7;color:#fff;font-size:9.5px;text-align:center;line-height:24px;border-radius:3px}
.bottom-bar{left:98px;top:1054px;width:768px;height:19px;background:var(--footer-bar);font-size:8px;color:#fff;font-weight:700;display:flex;justify-content:space-between;align-items:center;padding:0 25px 0 7px}
.bottom-bar .here{color:#8ed8cc;font-weight:400}
.bottom-bar .copy{font-weight:400;font-family:Jost,sans-serif}
</style>
</head>
<body>

<nav class="social-bar abs">
  <a class="item" href="#"><span class="dot" style="background:#8cc63f"></span>Email Us</a>
  <a class="item" href="#"><span class="dot" style="background:#3fb0e6"></span>VoiceLink</a>
  <a class="item" href="#"><span class="dot" style="background:#8fd3ea"></span>Chatter</a>
  <a class="item" href="#"><span class="dot" style="background:#3b5e9c"></span>FaceSpace</a>
</nav>

<div class="sheet abs"></div>
<div class="brand-name abs">Vinto PR</div>
<div class="call abs">Call us now <strong>0141 555 0199</strong></div>

<nav class="nav abs">
  <a class="current" href="#">Home</a>
  <a href="#">Real Services</a>
  <a href="#">Press Office</a>
  <a href="#">Real Case Studies</a>
  <a href="#">Real People</a>
  <a href="#">Blog</a>
  <a href="#">Real News</a>
  <a href="#">Contact us</a>
</nav>

<section class="banner abs">
  <div class="service-menu">
    <a class="active" style="top:10px" href="#">Online Public Relations</a>
    <a style="top:56px" href="#">Media Relations</a>
    <a style="top:94px" href="#">Consumer Campaigns</a>
    <a style="top:133px" href="#">Crisis Public Relations</a>
    <a style="top:171px" href="#">Internal Communications</a>
  </div>
  <div class="carousel" role="img" aria-label="Carousel photo of a crowd of pale 3D figures around a red target">
    <h2>Carousel</h2>
    <p>Showing sector specific service summary</p>
  </div>
</section>

<article class="intro abs">
  <h1>Introduction h1</h1>
  <p>Lorem ipsum dolor sit amet, consectetur adipiscing elit. Etiam bibendum posuere justo a lectus neque, pharetra a faucibus vel, vestibulum sed massa. Cum sociis natoque penati dis parturient montes, nascetur ridiculus mus. Nulla accumsan diam diam. Praesent non odio blandit viverra non vitae magna.</p>
  <p>haretra a faucibus vel, vestibulum sed massa. Cum sociis natoque penatibus et magnis dis parturient montes, nascetur ridiculus mus. Nulla accumsan diam diam. Praesent non odio blandit.</p>
  <p>us vel, vestibulum sed massa. Cum sociis natoque penatibus et magnis<br>dis parturient montes, nascetur.</p>
</article>

<section class="news abs" style="left:119px">
  <h3>Client News
    <svg width="16" height="16" viewBox="0 0 16 16"><rect width="16" height="16" rx="3" fill="#f08a24"/><circle cx="4.5" cy="11.5" r="1.6" fill="#fff"/><path d="M3 7a6 6 0 0 1 6 6M3 3.5a9.5 9.5 0 0 1 9.5 9.5" stroke="#fff" stroke-width="1.8" fill="none"/></svg>
  </h3>
  <p>Gismod, mauris vel biben du mfturingilla, fringilla, metutus dui vi fringilla, a artucu, vitae eleiffringilla.</p>
  <a class="more" href="#">read more</a>
</section>

<section class="news abs" style="left:364px">
  <h3>Blog Entry</h3>
  <div class="blog-img" role="img" aria-label="Photo of a blue and green nautilus shell"></div>
  <p>Gismod, mauris vel en du mfturingilla, fringilla, metutus dui ringilla, a artucu, vita e eleiffringilla.</p>
  <a class="more" href="#">read more</a>
</section>

<a class="c2a c2a-1 abs" href="#" role="img" aria-label="Call to action photo of a desk calendar page">C2A Button</a>
<a class="c2a c2a-2 abs" href="#" role="img" aria-label="Call to action photo of a businessman pointing">C2A Button</a>
<a class="c2a c2a-3 abs" href="#" role="img" aria-label="Call to action photo of red letter tiles spelling strategy"></a>
<a class="c2a c2a-4 abs" href="#" role="img" aria-label="Call to action photo of a man sketching a marketing diagram"></a>

<footer class="footer abs"></footer>
<div class="footer-links abs" style="left:119px">
  <a href="#">Online Public Relations</a><br>
  <a href="#">Media Relations</a><br>
  <a href="#">Consumer Campagns</a><br>
  <a href="#">Crisis Public Relations</a><br>
  <a href="#">Internal Communications</a>
</div>
<div class="footer-links abs" style="left:274px">
  <a href="#">Subscribe to RSS Feed</a><br>
  <a href="#">Our FaceSpace page</a><br>
  <a href="#">Link Three</a><br>
  <a href="#">Link Four</a>
</div>
<form class="enews abs">
  <h4>Enews Sign-up</h4>
  <div class="field">Email Address</div>
  <div class="btn">Subscribe</div>
</form>
<div class="bottom-bar abs">
  <span><span class="here">Home</span> | Real Services | Press Office | Real Case Studies | Real People | Blog | Real News | &nbsp;Contact us</span>
  <span class="copy">© 2010 Vinto PR All Rights Reserved</span>
</div>

</body>
</html>
```